Building Certification Company needs a professional letterhead and report template

We are a modern company within an ageing industry. Our industry is responsible for life safety aspects of the built environment, we ensure buildings are safe and fit for occupation.

We use letterhead and reports everyday, we need a smart and professional letterhead that reflects the serious nature of the work we do. We also require a report template of the same ilk.

Target Market(s)

Our target market will consist mainly of professional architects, developers and construction companies.

Requirements
Must have
• The letterhead must have:-
Our logo
Our company details, including address, website, email, phone

Address - Suite 208 / 43 Greyfern Avenue Tallowmere NSW 2100

Website - www.harbourlinestructureaudits.com.au

Email - info@hlsa.com.au

Phone - 02 8364 5208

The report template must have:-
A title page, which is to incorporate our logo or an aspect of our logo, get creative people.

```html
<!DOCTYPE html>
<html lang="en">
<head>
<meta charset="utf-8">
<title>Harbourline Structure Audits – Letterhead</title>
<link rel="stylesheet" href="https://fonts.googleapis.com/css2?family=Arimo:wght@400;700&display=swap">
<style>
  :root {
    --backdrop: #e6e7ea;
    --paper: #ffffff;
    --brand-blue: #5a6cc0;
    --brand-navy: #1f2c6e;
    --ink: #333333;
    --ink-soft: #555555;
    --signature-tone: #d9d9dd;
  }
  * { box-sizing: border-box; margin: 0; padding: 0; }
  html, body { width: 1200px; height: 800px; overflow: hidden; }
  body {
    background: var(--backdrop);
    font-family: "Arimo", Arial, sans-serif;
    color: var(--ink);
    display: flex;
    align-items: center;
    justify-content: center;
  }
  .letterhead {
    position: relative;
    width: 540px;
    height: 764px;
    background: var(--paper);
    box-shadow: 0 6px 22px rgba(0,0,0,0.18);
    padding: 30px 52px 0 58px;
  }
  .edge-band {
    position: absolute;
    left: 0; right: 0;
    background: var(--brand-blue);
  }
  .edge-band--top { top: 0; height: 6px; }
  .edge-band--bottom { bottom: 0; height: 24px; }
  .brand {
    display: flex;
    align-items: center;
    gap: 10px;
    margin-left: -8px;
  }
  .brand-square {
    width: 30px; height: 30px;
    background: var(--brand-navy);
  }
  .brand-name {
    font-weight: 700;
    font-size: 19px;
    letter-spacing: 0.02em;
    color: var(--brand-navy);
  }
  .letter-body {
    margin-top: 36px;
    font-size: 9.4px;
    line-height: 1.42;
    color: var(--ink-soft);
  }
  .salutation {
    font-weight: 700;
    color: var(--ink);
    margin-bottom: 12px;
  }
  .letter-body p { margin-bottom: 11px; }
  .sign-off {
    font-weight: 700;
    color: var(--ink);
    margin-top: 2px;
  }
  .signature {
    width: 84px;
    height: 30px;
    margin: 12px 0 6px 4px;
    background: var(--signature-tone);
    border-radius: 3px;
  }
  .signatory { font-weight: 700; color: var(--ink); }
  .contact-footer {
    position: absolute;
    left: 58px; right: 52px;
    bottom: 40px;
    font-size: 9.4px;
    line-height: 1.45;
    color: var(--ink-soft);
    display: flex;
    justify-content: space-between;
    align-items: flex-end;
  }
  .contact-footer strong { color: var(--ink); font-weight: 700; }
  .contact-footer .contact-secondary { margin-bottom: -2px; }
</style>
</head>
<body>
  <article class="letterhead">
    <div class="edge-band edge-band--top" role="img" aria-label="Blue and white diagonal stripe border"></div>

    <header class="brand">
      <span class="brand-square"></span>
      <span class="brand-name">Harbourline Structure Audits</span>
    </header>

    <section class="letter-body">
      <div class="salutation">Lorem<br>ipsum dolor sit amet,</div>
      <p>consectetur adipiscing elit. Duis facilisis elementum dui, bibendum pulvinar nulla malesuada quis. Curabitur id leo quam. Pellentesque laoreet metus risus, non fermentum arcu tortor suada vitae. Vestibulum dui libero, vestibulum non quam sit amet, varius congue erat. Integer blandit enim vitae adipiscing adipiscing. Vivamus metus nisl, dignissim at erat sed, pretium ut eros. Curabitur a dui interdum, pulvinar velit in, dictum nunc. Mauris feugiat odio sed dui rhoncus auctor. Aenean posuere odio et lorem blandit, eget convallis lacus ultricies. Donec in semper diam in velit vestibulum, sit amet molestie purus convallis. Duis pulvinar porttitor magna in malesuada.</p>
      <p>Nullam auctor neque orci, nec ornare odio auctor et. Phasellus eu sapien nec nibh lobortis commodo. Donec nec commodo nibh. Sed nec nulla et magna fermentum suscipit. Nam ligula nunc, facilisis vel iaculis venenatis eget, gravida consectetur odio. Donec in est vel lorem feugiat. In et orci in justo adipiscing vehicula. Sed tortor purus, pellentesque vel lobortis nec, tincidunt vitae mi. Duis pellentesque augue vitae pharetra euismod.</p>
      <p>Duis vulputate, libero nec vehicula pretium, mi nisi tristique mauris, ac porttitor diam metus at ante. Pellentesque magna arcu, viverra ac lacinia nec, pharetra id est. Maecenas ullamcorper mattis tellus, et dapibus arcu sagittis malesuada.</p>
      <p>Nam nulla turpis, dictum sit amet congue consequat, aliquet quis dolor. Curabitur cursus feugiat luctus.</p>
      <div class="sign-off">Nulla convallis</div>
      <div class="signature" role="img" aria-label="Handwritten signature"></div>
      <div class="signatory">volutpatnim.</div>
    </section>

    <footer class="contact-footer">
      <div class="contact-primary">
        <div><strong>Address:</strong> Suite 208 / 43 Greyfern Avenue Tallowmere NSW 2100</div>
        <div><strong>Website:</strong> www.harbourlinestructureaudits.com.au</div>
      </div>
      <div class="contact-secondary">
        <div><strong>Email:</strong> info@hlsa.com.au</div>
        <div><strong>Phone:</strong> 02 8364 5208</div>
      </div>
    </footer>

    <div class="edge-band edge-band--bottom" role="img" aria-label="Blue and white diagonal stripe border"></div>
  </article>
</body>
</html>
```